Business Card for IT company

I need a high tech looking business card using our logo. I prefer something clean and modern.

Target Market(s)

Buyers of IT hardware and software, IT Techies who are key influencers

Industry/Entity Type

Business

```html
<!DOCTYPE html>
<html lang="en">
<head>
<meta charset="utf-8">
<title>Norvale Consulting – Business Card</title>
<link rel="stylesheet" href="https://fonts.googleapis.com/css2?family=Source+Sans+3:wght@400;600;700&display=swap">
<style>
  :root {
    --page: #ececec;
    --card-light: #e6e6e6;
    --card-dark: #050505;
    --lime: #84ff00;
    --lime-deep: #4ce000;
    --ink: #111111;
    --ink-soft: #262b2b;
  }
  * { box-sizing: border-box; margin: 0; padding: 0; }
  html, body {
    width: 1200px; height: 1200px; overflow: hidden;
    background: var(--page);
    font-family: "Source Sans 3", "Myriad Pro", sans-serif;
  }
  .sheet { position: relative; width: 1200px; height: 1200px; }
  .card {
    position: absolute; left: 150px; width: 900px; height: 514px;
    border-radius: 26px; overflow: hidden;
    box-shadow: 0 6px 18px rgba(0,0,0,.18);
  }
  .card--front { top: 68px; background: var(--card-light); }
  .card--back { top: 618px; background: var(--card-dark); }

  .stripes { position: absolute; inset: 0; width: 100%; height: 100%; }

  .brand {
    position: absolute; left: 50px; top: 112px;
    display: flex; align-items: flex-start; gap: 12px;
    font-weight: 600; color: var(--ink-soft);
    font-size: 42px; line-height: 1.05;
  }
  .brand__mark {
    flex: none; width: 16px; height: 16px; border-radius: 50%;
    background: var(--ink-soft); margin-top: 15px;
  }

  .contact {
    position: absolute; right: 46px; top: 150px; text-align: right;
    color: var(--ink);
  }
  .contact__name {
    font-weight: 700; font-size: 46px; color: var(--lime-deep); line-height: 1;
  }
  .contact__title { font-size: 30px; line-height: 1.1; margin-bottom: 56px; }
  .contact__line { font-size: 28px; line-height: 1.3; }
  .contact__label { color: var(--lime-deep); }

  .back__circle {
    position: absolute; left: 50%; top: 50%;
    width: 590px; height: 590px; margin: -295px 0 0 -295px;
    border-radius: 50%; background: var(--lime);
  }
  .back__brand {
    position: absolute; left: 0; right: 0; top: 50%; transform: translateY(-50%);
    text-align: center; font-weight: 600; color: var(--ink-soft);
    font-size: 54px; letter-spacing: 1px;
  }
</style>
</head>
<body>
<main class="sheet">
  <section class="card card--front" aria-label="Business card front">
    <svg class="stripes" viewBox="0 0 900 514" preserveAspectRatio="none" aria-hidden="true">
      <polygon points="442,0 458,0 168,514 152,514" fill="#000"/>
      <polygon points="472,0 568,0 278,514 182,514" fill="#5cf000"/>
      <polygon points="582,0 598,0 308,514 292,514" fill="#000"/>
    </svg>
    <div class="brand"><span class="brand__mark"></span><span>Norvale<br>Consulting</span></div>
    <div class="contact">
      <p class="contact__name">Alden Marsh</p>
      <p class="contact__title">Consultant</p>
      <p class="contact__line"><span class="contact__label">P</span>: 123.456.7890</p>
      <p class="contact__line"><span class="contact__label">C</span>: 123.456.7890</p>
      <p class="contact__line"><span class="contact__label">E</span>: name@website.com</p>
      <p class="contact__line"><span class="contact__label">Add</span>: 1234 Main St, Your City, Sate, Zip.</p>
    </div>
  </section>

  <section class="card card--back" aria-label="Business card back">
    <div class="back__circle"></div>
    <div class="back__brand">Norvale Consulting</div>
  </section>
</main>
</body>
</html>
```